Webdesign für Lindenhof
Zielgruppe
Lindenhof Brauckmann:
Zielgruppe sind alle, die gern Fisch essen. Es gibt einen Hofladen, einen Partyservice, eine Gaststätte und eine kleine Pension. Wichtig wäre darzustellen, dass es in der Gaststätte außer Fisch auch Fleisch gibt.
Einen Einblick geben Ihnen die Webseite und der beiliegende Flyer.
Aufgabenstellung
Die Öffnungszeiten von Gaststätte und Hofladen sollten prominent dargestellt werden. Neben den eigenen Bildern sollen auch stock-Fotos genutzt werden.

```html
<!DOCTYPE html>
<html lang="de">
<head>
<meta charset="utf-8">
<title>Lindenhof Brauckmann – Webdesign</title>
<link rel="stylesheet" href="https://fonts.googleapis.com/css2?family=Source+Serif+4:wght@400;500&family=Overpass:wght@400;500&display=swap">
<style>
  :root {
    --white: #ffffff;
    --section-grey: #fafafa;
    --navy: #00304a;
    --heading-blue: #0b3f5c;
    --text-dark: #12324a;
    --accent: #0a9be0;
    --tile-dark: #26384a;
    --photo-sky: #b9c7d6;
    --photo-wall: #e6cf9f;
    --photo-wood: #9c3b22;
    --photo-green: #5d6f3a;
  }
  * { box-sizing: border-box; margin: 0; padding: 0; }
  html, body { width: 1200px; height: 850px; overflow: hidden; }
  body { background: var(--white); font-family: "Overpass", sans-serif; position: relative; }

  .service-row { position: absolute; top: 0; left: 0; width: 1200px; height: 169px; background: var(--white); }
  .service-tile {
    position: absolute; top: 0; width: 217px; height: 98px;
    display: flex; align-items: flex-end; justify-content: center; padding-bottom: 22px;
  }
  .tile-gaststaette { left: 134px; background: linear-gradient(180deg, #7a5a44 0%, #4b5a3a 45%, var(--tile-dark) 100%); }
  .tile-party { left: 373px; background: linear-gradient(180deg, #c8a873 0%, #7b6a55 45%, var(--tile-dark) 100%); }
  .tile-laden { left: 611px; background: linear-gradient(180deg, #6e6c6f 0%, #4f5a63 45%, var(--tile-dark) 100%); }
  .tile-pension { left: 848px; background: linear-gradient(180deg, #b8875a 0%, #6e6a66 45%, var(--tile-dark) 100%); }
  .tile-label {
    font-family: "Source Serif 4", serif; font-size: 24px; color: var(--white);
    line-height: 1; white-space: nowrap; padding-bottom: 3px;
  }
  .tile-label span { font-size: 16px; }
  .tile-label.is-active { border-bottom: 2px solid var(--white); }

  .intro { position: absolute; top: 169px; left: 0; width: 1200px; height: 442px; background: var(--section-grey); }
  .intro-ornament {
    position: absolute; left: 270px; top: 27px; width: 150px; height: 360px;
    background: radial-gradient(ellipse at center, rgba(200,205,210,0.18) 0%, rgba(250,250,250,0) 70%);
  }
  .intro-title {
    position: absolute; left: 188px; width: 300px; top: 96px;
    font-family: "Source Serif 4", serif; font-weight: 400; font-size: 39px; line-height: 42px;
    color: var(--heading-blue); text-align: center;
  }
  .intro-text {
    position: absolute; left: 180px; width: 316px; top: 206px;
    font-size: 12px; line-height: 18px; color: var(--text-dark); text-align: center;
  }
  .intro-button {
    position: absolute; left: 262px; top: 293px; width: 170px; height: 38px; border-radius: 19px;
    background: var(--accent); color: var(--white); display: flex; align-items: center; justify-content: center;
    font-family: "Source Serif 4", serif; font-size: 17px; text-decoration: none;
  }
  .intro-button span { font-size: 12px; margin-left: 4px; }
  .intro-photo {
    position: absolute; left: 563px; top: 61px; width: 506px; height: 294px;
    background: linear-gradient(180deg, #5a6470 0%, #5a6470 20%, var(--photo-wall) 30%, var(--photo-wood) 52%, #a9a39a 68%, var(--photo-green) 100%);
  }

  .news { position: absolute; top: 611px; left: 0; width: 1200px; height: 239px; background: var(--navy); color: var(--white); text-align: center; }
  .news-title { font-family: "Source Serif 4", serif; font-weight: 400; font-size: 39px; line-height: 1; margin-top: 70px; }
  .news-lead { font-size: 12px; margin-top: 12px; }
</style>
</head>
<body>
  <nav class="service-row">
    <a class="service-tile tile-gaststaette" role="img" aria-label="Foto: Garten vor der Hofgaststätte"><span class="tile-label">Hofgaststätte <span>»</span></span></a>
    <a class="service-tile tile-party" role="img" aria-label="Foto: angerichtete Fischplatte"><span class="tile-label">Partyservice <span>»</span></span></a>
    <a class="service-tile tile-laden" role="img" aria-label="Foto: Hofladen mit Blumen und Terrasse"><span class="tile-label is-active">Hofladen <span>»</span></span></a>
    <a class="service-tile tile-pension" role="img" aria-label="Foto: Holzbett im Pensionszimmer"><span class="tile-label">Pension <span>»</span></span></a>
  </nav>

  <section class="intro">
    <div class="intro-ornament" role="img" aria-label="Zarte Pflanzenzeichnung im Hintergrund"></div>
    <h1 class="intro-title">Der Lindenhof Brauckmann</h1>
    <p class="intro-text">Mit unserem Partyservice möchten wir dazu beitragen, dass Ihre Familienfeiern, Partys mit Freunden, Betriebsfeiern und Empfänge ein kulinarisches Erlebnis werden.</p>
    <a class="intro-button" href="#">Mehr erfahren <span>»</span></a>
    <div class="intro-photo" role="img" aria-label="Foto: Eingang der Hofgaststätte mit rotem Holzvordach und gepflastertem Weg"></div>
  </section>

  <section class="news">
    <h2 class="news-title">Aktuelles</h2>
    <p class="news-lead">Lorem ipsum dolor sit amet, consetetur sadipscing elitr</p>
  </section>
</body>
</html>
```